Clean and modern business cards

Looking for an updated business card design for my dental office “corvanta dental” . Looking for a modern clean / sleek design . I’m thinking black background but open to seeing other options . One side needs to have an appointment card . Card needs to have logo, dentist name , phone, email , address . I’ve attached couple of cards I thought were cool as well as my logo
Target Market(s)
Dental patients
Industry/Entity Type
Dentistry
Contact Information for Business Card
Phone email address

```html
<!DOCTYPE html>
<html lang="en">
<head>
<meta charset="utf-8">
<title>Corvanta Dental – Business &amp; Appointment Card</title>
<link href="https://fonts.googleapis.com/css2?family=Lexend:wght@300;400;700;800&display=swap" rel="stylesheet">
<style>
  :root {
    --canvas: #c9c9c9;
    --card-black: #030305;
    --lime: #8cf000;
    --lime-text: #8fe300;
    --field-fill: #e8f0ee;
    --white: #eef3f1;
  }
  * { margin: 0; padding: 0; box-sizing: border-box; }
  html, body { width: 1200px; height: 846px; overflow: hidden; }
  body {
    background: var(--canvas);
    font-family: "Lexend", sans-serif;
    position: relative;
  }
  .card {
    position: absolute;
    top: 169px;
    width: 291px;
    height: 508px;
    background: var(--card-black);
    overflow: hidden;
  }
  .card--front { left: 277px; }
  .card--appointment { left: 631px; }
  .card > * { position: absolute; }

  /* brand mark stand-in */
  .brand-dot {
    left: 50%; transform: translateX(-50%);
    top: 52px; width: 74px; height: 74px;
    border-radius: 50%;
    background: var(--lime);
  }
  .brand-name {
    left: 0; width: 100%; text-align: center;
    top: 146px;
    color: var(--white);
    font-weight: 700; font-size: 22px;
    letter-spacing: 1px;
    text-transform: uppercase;
    line-height: 1;
  }
  .brand-row {
    left: 28px; right: 28px; top: 70px;
    display: flex; align-items: center; gap: 10px;
  }
  .brand-row .dot {
    width: 40px; height: 40px; border-radius: 50%;
    background: var(--lime); flex: none;
  }
  .brand-row .name {
    color: var(--white);
    font-weight: 700; font-size: 19px;
    letter-spacing: 0.5px; text-transform: uppercase;
    line-height: 1.05;
  }

  .dentist-name {
    left: 0; width: 100%; text-align: center;
    top: 243px;
    color: var(--lime-text);
    font-weight: 800; font-size: 23px;
    letter-spacing: 0.5px;
  }
  .credentials {
    left: 0; width: 100%; text-align: center;
    top: 271px;
    color: var(--lime-text);
    font-weight: 300; font-size: 15px;
    letter-spacing: 0.3px;
  }
  .rule {
    left: 44px; width: 203px; height: 1px;
    background: var(--lime);
    opacity: 0.8;
  }
  .rule--top { top: 303px; }
  .rule--bottom { top: 379px; }

  .contact-line {
    left: 44px;
    display: flex; align-items: center; gap: 9px;
    color: var(--lime-text);
    font-weight: 300; font-size: 15px;
    letter-spacing: 0.3px;
  }
  .contact-line svg { width: 21px; height: 18px; flex: none; }
  .contact-line--phone { top: 317px; }
  .contact-line--email { top: 342px; }

  .address {
    left: 0; width: 100%; text-align: center;
    top: 393px;
    color: var(--lime-text);
    font-weight: 300; font-size: 15px;
    line-height: 20px;
  }

  .footer-band {
    left: 0; bottom: 0; width: 100%; height: 55px;
    border-top: 2px solid var(--lime);
    background: var(--card-black);
  }
  .footer-band span {
    position: absolute; left: 0; right: 0; bottom: 0; height: 52px;
    background: var(--lime);
    display: flex; align-items: center; justify-content: center;
    color: var(--card-black);
    font-weight: 800; font-size: 17px;
    letter-spacing: 0.4px;
  }

  .appointment-heading {
    left: 0; width: 100%; text-align: center;
    top: 159px;
    color: var(--lime-text);
    font-weight: 800; font-size: 19.5px;
    line-height: 24px;
    letter-spacing: 0.6px;
    text-transform: uppercase;
  }
  .field {
    left: 30px; width: 229px; height: 40px;
    background: var(--field-fill);
    border: 2px solid var(--lime);
    border-radius: 14px;
    padding-left: 7px;
    display: flex; align-items: center;
    color: var(--lime-text);
    font-weight: 800; font-size: 15px;
  }
  .field--date { top: 226px; }
  .field--time { top: 283px; }
  .cancel-notice {
    left: 0; width: 100%; text-align: center;
    top: 347px;
    color: var(--lime-text);
    font-weight: 300; font-size: 15px;
    line-height: 20.3px;
    letter-spacing: 0.3px;
  }
</style>
</head>
<body>

  <section class="card card--front" aria-label="Business card front">
    <div class="brand-dot"></div>
    <p class="brand-name">Corvanta Dental</p>

    <h1 class="dentist-name">Dr Lenar</h1>
    <p class="credentials">BSc (dent) DMD</p>

    <div class="rule rule--top"></div>
    <p class="contact-line contact-line--phone">
      <svg viewBox="0 0 24 20" fill="none" stroke="var(--lime)" stroke-width="2" stroke-linecap="round" stroke-linejoin="round" aria-hidden="true">
        <path d="M5 2l3 4-2 2c1 3 3 5 6 6l2-2 4 3-2 3C10 18 3 11 3 4z" fill="var(--lime)" stroke="none"/>
        <path d="M13 3a6 6 0 0 1 5 5"/>
        <path d="M13 0.5a9 9 0 0 1 8 8"/>
      </svg>
      (204) 555-0172
    </p>
    <p class="contact-line contact-line--email">
      <svg viewBox="0 0 24 18" fill="none" stroke="var(--lime)" stroke-width="2" stroke-linejoin="round" aria-hidden="true">
        <rect x="1.5" y="2" width="21" height="14"/>
        <path d="M1.5 2l10.5 8 10.5-8M1.5 16l8-7M22.5 16l-8-7"/>
      </svg>
      hello@corvantawpg.ca
    </p>
    <div class="rule rule--bottom"></div>

    <p class="address">214 – 880 Larchmere Ave,<br>Winnipeg, MB R2K 3T5</p>

    <div class="footer-band"><span>WWW.CORVANTAWPG.CA</span></div>
  </section>

  <section class="card card--appointment" aria-label="Appointment card">
    <div class="brand-row">
      <div class="dot"></div>
      <p class="name">Corvanta Dental</p>
    </div>

    <h2 class="appointment-heading">Your next<br>appointment is:</h2>

    <div class="field field--date">Date</div>
    <div class="field field--time">Time</div>

    <p class="cancel-notice">To cancel or reschedule<br>please notify us at least<br>48 hours prior to your<br>scheduled appointment</p>

    <div class="footer-band"><span>WWW.CORVANTAWPG.CA</span></div>
  </section>

</body>
</html>
```